Scholarly Growth Hub Business Cards

We need a business card for the Scholarly Growth Hub at Linwood Covenant College in Houston, TX. We are a Christian university. This card will be used to pass out to students who are interested in our free tutoring services. We offer several different services including an amazing study space with Vexor Screens, giant dry erase boards, collaborative furniture, and laptops. Students aren't as interested in printed documents. Our hope is that having something small like a business card, will encourage students to actually hold onto this.

Target Market(s)

College Students

Industry/Entity Type

College

Contact Information for Business Card

Scholarly Growth Hub
Linwood Covenant College
281.555.0187
sgh@lwcc.edu
www.lwcc.edu/sgh
Twitter: @SGH_LWCC

Font styles to use
Serif

Colors
0355a3

Requirements
Must have
• The information in the Business Card Details. We would like designs that utilize our school colors royal blue and orange. Those colors do not need to define the project, but can be used as highlights. Logo
Nice to have
• The 4 steps to making a tutoring appointment on the attached document.
• We want this to be sharp and eye catching.

```html
<!DOCTYPE html>
<html lang="en">
<head>
<meta charset="utf-8">
<title>Scholarly Growth Hub – Business Card</title>
<link rel="stylesheet" href="https://fonts.googleapis.com/css2?family=Open+Sans:wght@400;600&family=Arimo:wght@400;700&display=swap">
<style>
  :root {
    --stage: #3b3b3b;
    --paper: #f7f7f7;
    --royal: #0355a3;
    --orange: #c75a12;
    --step-red: #c63a0c;
    --ink: #4a4a4a;
    --lavender: #dcdcf4;
    --panel-grey: #6e6e70;
    --white: #ffffff;
    --black: #111111;
  }
  * { margin: 0; padding: 0; box-sizing: border-box; }
  html, body { width: 1200px; height: 750px; overflow: hidden; background: var(--stage); }
  .canvas { position: relative; width: 1200px; height: 750px; }
  .card {
    position: absolute; top: 228px; width: 461px; height: 262px; overflow: hidden;
  }
  .card--front { left: 124px; background: var(--paper); font-family: "Open Sans", sans-serif; }
  .card--back { left: 618px; background: var(--lavender); }

  .holder-name {
    position: absolute; left: 34px; top: 36px;
    font-size: 18px; font-weight: 600; color: var(--royal); letter-spacing: 0.2px;
  }
  .holder-title {
    position: absolute; left: 34px; top: 57px;
    font-size: 13px; color: var(--orange);
  }
  .rule {
    position: absolute; left: 36px; top: 83px; width: 384px; height: 2px; background: var(--orange);
  }
  .contact-list { position: absolute; left: 38px; top: 158px; list-style: none; }
  .contact-list li {
    display: flex; align-items: center; height: 17.6px;
    font-size: 12px; color: var(--ink);
  }
  .contact-list svg { width: 12px; height: 12px; margin-right: 8px; fill: var(--royal); }
  .back-art { display: block; width: 461px; height: 262px; font-family: "Arimo", sans-serif; }
</style>
</head>
<body>
<main class="canvas">

  <section class="card card--front" aria-label="Card front">
    <h1 class="holder-name">EVAN MARLOW</h1>
    <p class="holder-title">CEO/Founder</p>
    <div class="rule"></div>
    <ul class="contact-list">
      <li><svg viewBox="0 0 12 12" aria-hidden="true"><path d="M2.5 1h2l1 3-1.3 1a6.5 6.5 0 0 0 2.8 2.8L8 6.5l3 1v2c0 .8-.7 1.5-1.5 1.5A8.5 8.5 0 0 1 1 2.5C1 1.7 1.7 1 2.5 1z"/></svg>281.555.0187</li>
      <li><svg viewBox="0 0 12 12" aria-hidden="true"><path d="M1 3h10v6.5H1z M1.4 3.3 6 6.8l4.6-3.5" stroke="#f7f7f7" stroke-width=".8"/></svg>sgh@lwcc.edu</li>
      <li><svg viewBox="0 0 12 12" aria-hidden="true"><circle cx="6" cy="6" r="5.2"/><path d="M1 6h10M6 .8c-2 2.8-2 7.6 0 10.4M6 .8c2 2.8 2 7.6 0 10.4" stroke="#f7f7f7" stroke-width=".8" fill="none"/></svg>www.lwcc.edu/sgh</li>
      <li><svg viewBox="0 0 12 12" aria-hidden="true"><circle cx="6" cy="6" r="5"/></svg>@SGH_LWCC</li>
    </ul>
  </section>

  <section class="card card--back" aria-label="Card back: tutoring steps">
    <svg class="back-art" viewBox="0 0 461 262">
      <defs>
        <marker id="arrowhead" viewBox="0 0 6 6" refX="5" refY="3" markerWidth="5" markerHeight="5" orient="auto">
          <path d="M0 0L6 3L0 6z" fill="var(--black)"/>
        </marker>
      </defs>

      <rect class="title-panel" x="0" y="0" width="208" height="45" fill="var(--panel-grey)"/>
      <text x="104" y="20" text-anchor="middle" font-size="16" fill="var(--white)">Setting Up <tspan font-weight="700" text-decoration="underline">FREE</tspan> Tutoring</text>
      <text x="104" y="39" text-anchor="middle" font-size="16" fill="var(--white)">Appointment</text>

      <text class="hub-name" x="446" y="30" text-anchor="end" font-size="12" font-weight="700" fill="var(--royal)">Scholarly Growth Hub</text>

      <g class="flow-arrows" stroke="var(--black)" stroke-width="2" fill="none" marker-end="url(#arrowhead)">
        <path d="M114 84V66H184"/>
        <path d="M270 84H312V98"/>
        <path d="M296 194V208H233"/>
        <path d="M203 156V144H156"/>
      </g>

      <g class="step-markers" fill="var(--step-red)">
        <circle cx="229" cy="78" r="35"/>
        <circle cx="306" cy="136" r="35"/>
        <circle cx="196" cy="190" r="35"/>
        <circle cx="115" cy="130" r="35"/>
      </g>
      <g class="step-numbers" font-size="40" font-weight="700" fill="var(--white)">
        <text x="192" y="98">1</text>
        <text x="270" y="155">2</text>
        <text x="205" y="218">3</text>
        <text x="100" y="158">4</text>
      </g>

      <g class="step-copy" font-size="9" font-weight="700" fill="var(--black)" text-anchor="middle">
        <text x="292" y="56">Go to www.my.lwcc.edu, log-in,</text>
        <text x="292" y="67">and click the “Navigate” icon on the</text>
        <text x="292" y="78">top left of the home screen.</text>

        <text x="352" y="126">Click “Home” followed by</text>
        <text x="352" y="137">“Courses I'm Taking.”</text>

        <text x="132" y="188">If tutoring is available for the</text>
        <text x="132" y="198">course, click “Schedule Online”</text>
        <text x="132" y="208">under the listing.</text>

        <text x="113" y="95">Bolded dates on the calendar</text>
        <text x="113" y="105">represent available</text>
        <text x="113" y="115">appointments. Select desired</text>
        <text x="113" y="125">date and time to book.</text>
      </g>

      <rect class="note-box" x="282" y="148" width="131" height="44" fill="none" stroke="var(--black)" stroke-width="1"/>
      <g font-size="7" fill="var(--black)" text-anchor="middle">
        <text x="347" y="157">If tutoring is available for the</text>
        <text x="347" y="167">course, it will be by the course</text>
        <text x="347" y="177">listing and titled “SGH: <tspan font-style="italic">SUBJECT</tspan></text>
        <text x="347" y="187">Tutoring.”</text>
      </g>

      <rect class="deadline-panel" x="229" y="218" width="232" height="44" fill="var(--panel-grey)"/>
      <text x="345" y="236" text-anchor="middle" font-size="16" fill="var(--white)">Book by 5pm the day</text>
      <text x="345" y="255" text-anchor="middle" font-size="16" fill="var(--white)">before desired appointment</text>
    </svg>
  </section>

</main>
</body>
</html>
```